English and Spanish Language School Needs a Business Card

Need a business card design a startup company called Corvelle Language School. The company will offer English and Spanish conversational level courses designed to make the learner feel comfortable with grammar and vocabulary. We would like to see a logo with some colour that should communicate learning, growth.

Target Market(s)

Consumers and businesses

Industry/Entity Type

Education

Contact Information for Business Card

TBD

Font styles to use
Serif

Requirements
Must have
• Include the following
• Logo
• Name
• Title
• Cellphone Number
• Office Phone number
• Email address
• Office Address

```html
<!DOCTYPE html>
<html lang="en">
<head>
<meta charset="utf-8">
<title>Corvelle Language School – Business Card</title>
<link href="https://fonts.googleapis.com/css2?family=Quicksand:wght@400;500;700&display=swap" rel="stylesheet">
<style>
  :root {
    --stage: #e9e7e3;
    --card: #ffffff;
    --red: #d8262f;
    --teal: #2cc3c9;
    --ink: #333333;
    --muted: #555555;
  }
  * { box-sizing: border-box; margin: 0; padding: 0; }
  html, body { width: 780px; height: 1200px; overflow: hidden; }
  body {
    background: var(--stage);
    font-family: "Quicksand", sans-serif;
    color: var(--ink);
    position: relative;
  }
  .card {
    position: absolute;
    left: 70px;
    width: 640px;
    height: 366px;
    background: var(--card);
    box-shadow: 0 6px 18px rgba(0,0,0,.12);
    overflow: hidden;
  }
  .card--front { top: 170px; }
  .card--back { top: 664px; }
  .card__shapes { position: absolute; inset: 0; width: 100%; height: 100%; }

  .brand {
    position: absolute;
    color: var(--red);
    font-weight: 700;
    line-height: 1;
    background: var(--card);
  }
  .brand__name { display: block; letter-spacing: .5px; }
  .brand__tag { display: block; }

  .card--front .brand { right: 34px; top: 92px; padding: 6px 10px; text-align: right; }
  .card--front .brand__name { font-size: 40px; }
  .card--front .brand__tag { font-size: 13px; margin-top: 4px; }

  .holder {
    position: absolute;
    left: 40px;
    top: 232px;
    padding-left: 16px;
    border-left: 4px solid var(--red);
  }
  .holder__name { font-size: 27px; font-weight: 400; color: var(--ink); }
  .holder__title { font-size: 14px; font-weight: 500; color: var(--teal); margin-top: 2px; }

  .contacts {
    position: absolute;
    left: 330px;
    top: 218px;
    list-style: none;
  }
  .contacts li {
    display: flex;
    align-items: center;
    gap: 10px;
    font-size: 15px;
    font-weight: 500;
    color: var(--muted);
    height: 27px;
  }
  .contacts svg { width: 14px; height: 14px; fill: var(--teal); flex: none; }

  .card--back .brand { left: 262px; top: 118px; background: transparent; }
  .card--back .brand__name { font-size: 78px; }
  .card--back .brand__tag { font-size: 23px; margin-top: 6px; padding-left: 4px; }
</style>
</head>
<body>

  <section class="card card--front" aria-label="Business card front">
    <svg class="card__shapes" viewBox="0 0 640 366" aria-hidden="true">
      <polygon points="430,0 462,0 640,178 640,210" fill="var(--red)"/>
      <polygon points="486,0 514,0 640,126 640,154" fill="var(--teal)"/>
    </svg>

    <div class="brand">
      <span class="brand__name">Corvelle</span>
      <span class="brand__tag">Language School</span>
    </div>

    <div class="holder">
      <p class="holder__name">Your Name</p>
      <p class="holder__title">Job Title</p>
    </div>

    <ul class="contacts">
      <li>
        <svg viewBox="0 0 16 16"><path d="M2 4c0-1 1-2 2-2h8c1 0 2 1 2 2v2h-3V5H5v1H2zM3 7h10l1 7H2zm5 2a2 2 0 100 4 2 2 0 000-4z"/></svg>
        000 000 0000
      </li>
      <li>
        <svg viewBox="0 0 16 16"><path d="M4 1h8v14H4zm1.5 1.5v9h5v-9zM7 12.5h2v1H7z" fill-rule="evenodd"/></svg>
        000 000 0000
      </li>
      <li>
        <svg viewBox="0 0 16 16"><path d="M1 3h14v10H1zm1.5 1.5L8 9l5.5-4.5z" fill-rule="evenodd"/></svg>
        youremail@corvelle.test
      </li>
      <li>
        <svg viewBox="0 0 16 16"><path d="M8 1a5 5 0 015 5c0 4-5 9-5 9S3 10 3 6a5 5 0 015-5zm0 3a2 2 0 100 4 2 2 0 000-4z" fill-rule="evenodd"/></svg>
        address, here- 0000
      </li>
    </ul>
  </section>

  <section class="card card--back" aria-label="Business card back">
    <svg class="card__shapes" viewBox="0 0 640 366" aria-hidden="true">
      <polygon points="0,100 477,366 387,366 0,150" fill="var(--teal)"/>
      <polygon points="0,160 370,366 280,366 0,210" fill="var(--red)"/>
      <polygon points="0,252 0,366 204,366" fill="var(--red)"/>
    </svg>

    <div class="brand">
      <span class="brand__name">Corvelle</span>
      <span class="brand__tag">Language School</span>
    </div>
  </section>

</body>
</html>
```